Relationship Seminar

I am an Author and Speaker and I need a flyer for a Christian relationship seminar targeting women aged between mid 20's to late 30's. It's an event for women only.

-I am looking for a fresh/ edgy look but still feminine
-Nothing too girly
-Maximum of 3 colours (Spring colours are good)
-I want the flyer to convey joy or happiness
-Use my photo which is attached as the predominant image (you can crop it to remove the background etc)

The Flyer Details are as follows:

Somewhere Past Tomorrow - Brisbane Tour

Join Author & Speaker, Rosalind Okafe, as she speaks about her new book entitled 'Somewhere Past Tomorrow'.

Be inspired and encouraged to embrace the life that God has given you and make the most of it!

Date: Saturday 9th November 2013
Time: 2:00 pm - 5:00 pm
Location: Larkwell Hotel Brisbane (Juniper Ballroom)
Fennimore Street, Brisbane QLD 4000
Tickets: $60/pp (Includes High Tea)
Buy Tickets: www.rosalindokafe.com or http://somewherepasttomorrow.ticketvane.net

Email: info@rosalindokafe.com

Include the cover of my new book.

www.rosalindokafe.com (include my website at the bottom of the flyer)

Target Market(s)

Young professional women aged between their mid 20's to late 30's

Industry/Entity Type

Event

Requirements
Should not have
• -No girly or curly font

```html
<!DOCTYPE html>
<html lang="en">
<head>
<meta charset="utf-8">
<title>Somewhere Past Tomorrow – Brisbane Tour</title>
<link rel="stylesheet" href="https://fonts.googleapis.com/css2?family=Anton&family=Arimo:wght@400;700&family=Rammetto+One&family=Tinos&display=swap">
<style>
  :root {
    --flyer-yellow: #f7ef45;
    --panel-yellow: #fff51f;
    --accent-red: #c4203a;
    --cover-light: #eef0ee;
    --cover-shade: #b9c2c4;
    --portrait-dark: #2a2424;
    --portrait-warm: #6b4a3c;
  }
  * { margin: 0; padding: 0; box-sizing: border-box; }
  html, body { width: 927px; height: 1200px; overflow: hidden; background: var(--flyer-yellow); }
  .flyer { position: relative; width: 927px; height: 1200px; background: var(--flyer-yellow); }
  .flyer__art { position: absolute; inset: 0; }
  .kicker { font-family: "Rammetto One", Georgia, serif; font-size: 21px; fill: var(--accent-red); }
  .speaker-name { font-family: "Rammetto One", Georgia, serif; font-size: 72px; fill: var(--accent-red); }
  .intro-line { font-family: "Rammetto One", Georgia, serif; font-size: 15px; fill: var(--accent-red); }
  .book-title { font-family: "Anton", Impact, sans-serif; font-size: 124px; fill: var(--accent-red); }
  .tour-line { font-family: "Anton", Impact, sans-serif; font-size: 28px; letter-spacing: 6px; fill: var(--accent-red); }
  .event-details {
    position: absolute; left: 398px; top: 680px;
    font-family: "Arimo", Arial, sans-serif; font-size: 17px; line-height: 24.6px;
    color: var(--accent-red); list-style: none;
  }
  .event-details .indent { padding-left: 102px; }
  .event-details .indent-wide { padding-left: 130px; }
  .tagline {
    position: absolute; left: 48px; top: 985px; width: 500px;
    font-family: "Arimo", Arial, sans-serif; font-weight: 700; font-size: 20px; line-height: 28px;
    color: var(--accent-red);
  }
  .site-footer {
    position: absolute; left: 48px; top: 1128px;
    font-family: "Tinos", "Times New Roman", serif; font-size: 33px; color: var(--accent-red);
  }
</style>
</head>
<body>
<main class="flyer">
  <svg class="flyer__art" width="927" height="1200" viewBox="0 0 927 1200">
    <defs>
      <linearGradient id="coverFill" x1="0" y1="0" x2="1" y2="1">
        <stop offset="0" stop-color="var(--cover-light)"/>
        <stop offset="1" stop-color="var(--cover-shade)"/>
      </linearGradient>
      <linearGradient id="portraitFill" x1="0" y1="0" x2="0" y2="1">
        <stop offset="0" stop-color="var(--portrait-warm)"/>
        <stop offset="1" stop-color="var(--portrait-dark)"/>
      </linearGradient>
    </defs>

    <text class="kicker" transform="translate(50 197) rotate(-14)">Join Author and Speaker</text>

    <text class="speaker-name" x="463" y="305" text-anchor="middle" textLength="590" lengthAdjust="spacingAndGlyphs">ROSALIND OKAFE</text>

    <text class="intro-line" x="459" y="377" text-anchor="middle">as she speaks about her new book entitled</text>

    <text class="book-title" x="473" y="565" text-anchor="middle" textLength="840" lengthAdjust="spacingAndGlyphs">“SOMEWHERE PAST TOMORROW”</text>

    <text class="tour-line" x="464" y="612" text-anchor="middle">BRISBANE TOUR</text>

    <g class="book-panel">
      <rect x="58" y="640" width="292" height="316" fill="var(--panel-yellow)" transform="rotate(-5 204 798)"/>
      <rect x="135" y="652" width="140" height="292" fill="url(#coverFill)" role="img" aria-label="Cover of the book Somewhere Past Tomorrow"/>
    </g>

    <g class="portrait-panel">
      <rect x="596" y="900" width="290" height="290" fill="var(--panel-yellow)" transform="rotate(-8 741 1045)"/>
      <rect x="626" y="918" width="232" height="282" rx="90" fill="url(#portraitFill)" role="img" aria-label="Portrait photo of Rosalind Okafe"/>
    </g>
  </svg>

  <ul class="event-details">
    <li>Date : Saturday, November 09, 2013</li>
    <li>Time : 2:00 p.m. to 5:00 p.m.</li>
    <li>Location : Larkwell Hotel Brisbane (Juniper Ballroom)</li>
    <li class="indent">Fennimore Street, Brisbane QLD 4000</li>
    <li>Ticket price : $60/pp (Includes High Tea)</li>
    <li>Buy Ticket : www.rosalindokafe.com or</li>
    <li class="indent-wide">http://somewherepasttomorrow.ticketvane.net</li>
    <li>Email : info@rosalindokafe.com</li>
  </ul>

  <p class="tagline">Be inspired and encouraged to embrace the life that God has given you and make the most of it!</p>

  <footer class="site-footer">www.rosalindokafe.com</footer>
</main>
</body>
</html>
```